Redesign von Homepage lumo werke
Aufgabenstellung
Benötigt wird eine optisch verbesserte Version der aktuellen Homepage www.lumo-werke.de. Struktur und Inhalt sollen bleiben. Widgets wie Kalender und Anmeldung sind kein Muss.
Ein Plus wäre es, wenn anstatt des HTML-Template ein Joomla- oder Wordpress-Template geliefert werden könnte. Besonders deshalb, weil wir innerhalb des nächsten Jahres einen finalen Webauftritt mit neuen Inhalten und neuer Struktur planen. Der zukünftige Webauftritt soll dann nach Möglichkeit mit dem Gewinner des vorliegenden Projekts umgesetzt werden.

```html
<!DOCTYPE html>
<html lang="de">
<head>
<meta charset="utf-8">
<title>lumo werke – Startseite</title>
<link href="https://fonts.googleapis.com/css2?family=PT+Sans:ital,wght@0,400;0,700;1,400&display=swap" rel="stylesheet">
<style>
:root{
  --orange:#f28c16;
  --orange-light:#f9a83a;
  --orange-dark:#e07708;
  --ink:#2e2e2e;
  --text:#6b6b6b;
  --muted:#9a9a9a;
  --line:#e2e2e2;
  --panel:#f3f3f3;
  --white:#ffffff;
}
*{margin:0;padding:0;box-sizing:border-box}
html,body{width:1200px;height:1123px;overflow:hidden;background:var(--white);font-family:'PT Sans',Arial,sans-serif;color:var(--text)}
.page{position:relative;width:1200px;height:1123px}

/* header */
.site-header{position:absolute;left:0;top:0;width:1200px;height:92px;background:linear-gradient(#ffffff,#f2f2f2)}
.brand{position:absolute;left:136px;top:30px;font-size:30px;font-weight:700;color:var(--ink);line-height:1}
.main-nav{position:absolute;left:585px;top:0;display:flex;height:92px}
.main-nav a{display:block;width:135px;padding:36px 0 0 28px;border-left:1px solid var(--line);text-decoration:none}
.main-nav a:first-child{border-left:none}
.nav-title{display:block;font-size:19px;font-weight:700;color:var(--ink)}
.nav-sub{display:block;font-size:9px;letter-spacing:1px;color:var(--muted);text-transform:uppercase}

/* hero */
.hero{position:absolute;left:0;top:92px;width:1200px;height:268px;background:linear-gradient(180deg,var(--orange-light) 0%,var(--orange) 55%,var(--orange-dark) 100%)}
.hero-photo{position:absolute;left:149px;top:24px;width:513px;height:244px;background:linear-gradient(135deg,#c9ccd0,#8b8f96 55%,#55575c);border:4px solid var(--white);border-bottom:none;box-shadow:0 4px 14px rgba(0,0,0,.3)}
.slider-dots{position:absolute;left:502px;top:238px;display:flex;gap:8px}
.slider-dots span{width:12px;height:12px;border-radius:50%;background:rgba(255,255,255,.55)}
.slider-dots span:first-child{background:var(--white)}
.hero-copy{position:absolute;left:667px;top:70px;width:390px;color:var(--white)}
.hero-copy h1{font-size:26px;font-weight:700;margin-bottom:12px}
.hero-copy p{font-size:14px;line-height:1.5}

/* features */
.features{position:absolute;left:144px;top:396px;width:912px;display:flex;gap:48px}
.feature{width:252px;position:relative;padding-bottom:14px;border-bottom:1px solid var(--line);height:194px}
.feature-head{display:flex;align-items:flex-end;gap:8px;height:50px}
.feature-icon{width:40px;height:46px;background:linear-gradient(#7a7a7a,#2f2f2f);border-radius:3px}
.feature-title{font-size:17px;font-weight:700;color:var(--orange);line-height:1}
.feature-sub{font-size:12px;font-weight:700;color:var(--ink)}
.feature p{margin-top:18px;padding-left:30px;font-size:12px;line-height:1.45}
.feature p b{color:var(--ink)}
.read-more{position:absolute;right:0;bottom:6px;font-size:12px;font-weight:700;color:var(--ink);text-decoration:underline}

/* testimonial */
.testimonial{position:absolute;left:139px;top:612px;width:864px;height:80px;background:var(--panel);border-radius:4px;display:flex;align-items:center}
.testimonial-label{width:158px;padding-left:24px;font-size:12px;font-weight:700;color:var(--orange)}
.testimonial-quote{width:620px;padding-left:16px;border-left:1px solid var(--line);font-size:11px;font-style:italic;line-height:1.45}
.testimonial-nav{position:absolute;right:18px;top:54px;display:flex;gap:8px}

/* content */
.intro{position:absolute;left:156px;top:744px;width:560px}
.intro h2{font-size:18px;font-weight:400;color:var(--ink);line-height:1.3;margin-bottom:24px}
.intro p{font-size:11.5px;line-height:1.5;color:var(--muted);margin-bottom:16px}

.news{position:absolute;left:744px;top:715px;width:259px;height:221px;background:var(--panel);border-radius:4px;box-shadow:0 2px 6px rgba(0,0,0,.08)}
.news-tab{position:absolute;left:0;top:0;width:92px;height:28px;background:var(--orange);color:var(--white);font-size:12px;font-weight:700;line-height:28px;text-align:center;border-radius:4px 4px 4px 0}
.news ul{list-style:none;position:absolute;left:28px;top:42px;width:210px}
.news li{font-size:11.5px;line-height:1.4;padding:10px 0 10px 18px;border-bottom:1px solid var(--line);position:relative}
.news li:last-child{border-bottom:none}
.news li::before{content:"";position:absolute;left:2px;top:15px;width:5px;height:5px;border-radius:50%;background:var(--muted)}
.news li.active{color:var(--orange)}
.news li.active::before{background:var(--orange)}

/* footer */
.site-footer{position:absolute;left:120px;top:1051px;width:890px;border-top:1px solid var(--line)}
.footer-nav{position:absolute;left:0;top:30px;display:flex;gap:34px;font-size:12px;color:var(--muted)}
.footer-brand{position:absolute;right:0;top:30px;font-size:12px;color:var(--muted)}
</style>
</head>
<body>
<div class="page">
  <header class="site-header">
    <div class="brand">lumo werke</div>
    <nav class="main-nav">
      <a href="#"><span class="nav-title">Home</span><span class="nav-sub">Startseite</span></a>
      <a href="#"><span class="nav-title">About us</span><span class="nav-sub">Wer wir sind</span></a>
      <a href="#"><span class="nav-title">References</span><span class="nav-sub">Was wir tun</span></a>
      <a href="#"><span class="nav-title">Contact</span><span class="nav-sub">Schreiben Sie</span></a>
    </nav>
  </header>

  <section class="hero">
    <div class="hero-photo" role="img" aria-label="Foto: Geschäftsleute bei einer Besprechung am Laptop"></div>
    <div class="slider-dots"><span></span><span></span><span></span><span></span></div>
    <div class="hero-copy">
      <h1>Lorem ipsum dolor sit amet</h1>
      <p>Lorem ipsum dolor sit amet, consectetuer adipiscing elit. Aenean commodo ligula eget dolor. Aenean massa. Cum sociis natoque penatibus et magnis dis parturient montes, nascetur ridiculus mus.</p>
    </div>
  </section>

  <section class="features">
    <article class="feature">
      <div class="feature-head"><div class="feature-icon" role="img" aria-label="Symbol: Person"></div><div><div class="feature-title">About us</div><div class="feature-sub">Who we are</div></div></div>
      <p>Lorem ipsum dolor sit amet, consetetur sadipscing elitr, sed diam nonumy eirmod tempor invidunt ut labore et dolore magna <b>aliquyam erat</b>, sed diam voluptua. At vero eos et accusam et justo duo dolores et ea rebum.</p>
      <a class="read-more" href="#">read more</a>
    </article>
    <article class="feature">
      <div class="feature-head"><div class="feature-icon" role="img" aria-label="Symbol: Diagramm"></div><div><div class="feature-title">Lorem ipsum Ip</div><div class="feature-sub">What is it</div></div></div>
      <p>Lorem ipsum dolor sit amet, consetetur sadipscing elitr, sed diam nonumy eirmod tempor invidunt ut labore et dolore magna <b>aliquyam erat</b>, sed diam voluptua. At vero eos et accusam et justo duo dolores et ea rebum.</p>
      <a class="read-more" href="#">read more</a>
    </article>
    <article class="feature">
      <div class="feature-head"><div class="feature-icon" role="img" aria-label="Symbol: Firmengebäude"></div><div><div class="feature-title">Company</div><div class="feature-sub">The company</div></div></div>
      <p>Lorem ipsum dolor sit amet, consetetur sadipscing elitr, sed diam nonumy eirmod tempor invidunt ut labore et dolore magna <b>aliquyam erat</b>, sed diam voluptua. At vero eos et accusam et justo duo dolores et ea rebum.</p>
      <a class="read-more" href="#">read more</a>
    </article>
  </section>

  <section class="testimonial">
    <div class="testimonial-label">Kundenstimmen</div>
    <div class="testimonial-quote">"Lorem ipsum dolor sit amet, consetetur sadipscing elitr, sed diam nonumy eirmod tempor invidunt ut labore et dolore magna aliquyam erat, sed diam voluptua. At vero eos et accusam et justo duo dolores et ea rebum. Stet clita kasd gubergren, no sea takimata sanctus est Lorem ipsum dolor sit amet."</div>
    <div class="testimonial-nav">
      <svg width="10" height="12" viewBox="0 0 10 12"><path d="M9 1 2 6l7 5z" fill="#555"/></svg>
      <svg width="10" height="12" viewBox="0 0 10 12"><path d="M1 1l7 5-7 5z" fill="#555"/></svg>
    </div>
  </section>

  <section class="intro">
    <h2>Lorem ipsum dolor sit amet, consetetur sadipscing elitr, sed diam nonumy eirmod tempor invidunt ut labore et dolore</h2>
    <p>magna aliquyam erat, sed diam voluptua. At vero eos et accusam et justo duo dolores et ea rebum. Stet clita kasd gubergren, no sea takimata sanctus est Lorem ipsum dolor sit amet. Lorem ipsum dolor sit amet, consetetur sadipscing elitr, sed diam nonumy eirmod tempor invidunt ut labore et dolore magna aliquyam erat, sed diam voluptua. At vero eos et accusam et justo duo dolores et ea rebum.</p>
    <p>Stet clita kasd gubergren, no sea takimata sanctus est Lorem ipsum dolor sit amet.</p>
  </section>

  <aside class="news">
    <div class="news-tab">Aktuelles</div>
    <ul>
      <li>Lorem ipsum dolor sit amet</li>
      <li class="active">consetetur sadipscing elitr, sed diam nonumy eirmod tempor</li>
      <li>invidunt ut labore</li>
      <li>et dolore magna aliquyam erat, sed diam voluptua</li>
    </ul>
  </aside>

  <footer class="site-footer">
    <nav class="footer-nav"><span>Home</span><span>About us</span><span>References</span><span>Blog</span><span>Contact</span><span>Impress</span></nav>
    <div class="footer-brand">Copyright by lumo werke</div>
  </footer>
</div>
</body>
</html>
```